You are cordially invited to attend a delicious Afternoon Tea at The Ashcombe.

Enjoy a glass of sparkling wine whilst afternoon delicacies and a menu of fine teas is presented for you to enjoy throughout the afternoon.

This is an opportunity to get together with a table of like minded ladies just for fun and to share some stories and meet some new friends.

Date: 8 August 2014
Time: 12pm - 2pm
Venue: 47 Larkfield Street, Melbourne VIC 3000

(hello please see above text we require - we would like to invite our clients to an afternoon tea, an invitation (hard copy) to be of elegant taste, nice lettering, pic added to the invite).

```html
<!DOCTYPE html>
<html lang="en">
<head>
<meta charset="utf-8">
<title>Afternoon Tea at The Ashcombe</title>
<link href="https://fonts.googleapis.com/css2?family=Questrial&display=swap" rel="stylesheet">
<style>
  :root {
    --page: #ffffff;
    --card: #ebe8e3;
    --ink: #3a2718;
    --ink-soft: #4a3222;
    --rule: #4a3222;
    --tone-edge: #ddd3c2;
    --tone-warm: #c8b083;
    --tone-deep: #b99d6e;
  }
  html, body {
    margin: 0;
    padding: 0;
    width: 1200px;
    height: 789px;
    overflow: hidden;
    background: var(--page);
  }
  .invitation {
    position: relative;
    width: 1200px;
    height: 789px;
    font-family: "Questrial", "Century Gothic", sans-serif;
    color: var(--ink);
  }
  .invitation__card {
    position: absolute;
    left: 27px;
    top: 22px;
    width: 1146px;
    height: 743px;
    background: var(--card);
  }
  .invitation__heading {
    position: absolute;
    left: 0;
    top: 125px;
    width: 1200px;
    margin: 0;
    text-align: center;
    font-weight: 400;
    font-size: 23.5px;
    line-height: 30px;
    letter-spacing: 0.3px;
    text-transform: uppercase;
    white-space: nowrap;
    color: var(--ink);
  }
  .tea-photo {
    position: absolute;
    left: 27px;
    top: 222px;
    width: 1146px;
    height: 270px;
    background: linear-gradient(90deg,
      var(--tone-edge) 0%,
      var(--tone-edge) 12%,
      var(--tone-warm) 25%,
      var(--tone-deep) 50%,
      var(--tone-warm) 75%,
      var(--tone-edge) 88%,
      var(--tone-edge) 100%);
  }
  .event-details {
    position: absolute;
    right: 760px;
    top: 551px;
    margin: 0;
    text-align: right;
    font-size: 40px;
    line-height: 40.5px;
    color: var(--ink);
  }
  .event-details span { display: block; white-space: nowrap; }
  .divider {
    position: absolute;
    left: 492px;
    top: 543px;
    width: 2px;
    height: 185px;
    background: var(--rule);
  }
  .event-blurb {
    position: absolute;
    left: 538px;
    top: 538px;
    font-size: 24px;
    line-height: 27px;
    letter-spacing: 0.8px;
    color: var(--ink-soft);
  }
  .event-blurb p { margin: 0 0 24px; white-space: nowrap; }
</style>
</head>
<body>
  <main class="invitation">
    <div class="invitation__card"></div>

    <h1 class="invitation__heading">You are cordially invited to attend a delicious afternoon tea at The Ashcombe</h1>

    <div class="tea-photo" role="img" aria-label="Photograph of an elegant tea room table set for afternoon tea with cakes, teapots, cups and sparkling wine"></div>

    <p class="event-details">
      <span>On 8 August 2014</span>
      <span>From12pm - 2pm</span>
      <span>At 47 Larkfield Street</span>
      <span>Melbourne VIC 3000</span>
    </p>

    <div class="divider"></div>

    <div class="event-blurb">
      <p>Enjoy a glass of sparkling wine whilst afternoon<br>delicacies and a menu of fine teas is presented<br>for you to enjoy throughout the afternoon.</p>
      <p>This is an opportunity to get together with a table<br>of like minded ladies just for fun and to share<br>some stories and meet some new friends.</p>
    </div>
  </main>
</body>
</html>
```